stationary for hygienic company

We need a stationary design for hygienic company which provides public high end sanitary products and high end public lavatory.
We need a fresh and clean style stationary
we want the following things:
* logo (redesigned in eps/vector)
* Letterhead (with company details)
* letterhead (without company details)
* Business card
* note block
* ballpoint
* etcetera (a complete package)

```html
<!DOCTYPE html>
<html lang="en">
<head>
<meta charset="utf-8">
<title>Clarevo Stationery</title>
<link href="https://fonts.googleapis.com/css2?family=Questrial&family=Poppins:wght@400;600&display=swap" rel="stylesheet">
<style>
  :root {
    --backdrop: #dcdcdc;
    --paper: #ffffff;
    --magenta: #e8008a;
    --navy: #0a0082;
    --sky: #00adec;
    --ink: #111111;
    --muted: #8a8a8a;
  }
  html, body {
    margin: 0;
    padding: 0;
    overflow: hidden;
  }
  .canvas {
    position: relative;
    width: 1200px;
    height: 900px;
    background: var(--backdrop);
    overflow: hidden;
  }
  .sheet {
    position: absolute;
    top: 93px;
    width: 503px;
    height: 712px;
    background: var(--paper);
    overflow: hidden;
  }
  .sheet--cover { left: 74px; }
  .sheet--letterhead { left: 608px; }

  .cover-panel {
    position: absolute;
    left: 0;
    top: 0;
    width: 503px;
    height: 600px;
    background: linear-gradient(135deg, var(--magenta) 0%, var(--navy) 50%, var(--sky) 100%);
  }
  .cover-url {
    position: absolute;
    right: 24px;
    bottom: 20px;
    margin: 0;
    font-family: "Poppins", sans-serif;
    font-weight: 600;
    font-size: 12.5px;
    color: var(--ink);
    letter-spacing: 0.2px;
  }

  .brand {
    position: absolute;
    left: 27px;
    top: 76px;
    display: flex;
    align-items: center;
    gap: 10px;
  }
  .brand-dot {
    width: 16px;
    height: 16px;
    border-radius: 50%;
    background: var(--navy);
  }
  .brand-name {
    margin: 0;
    font-family: "Questrial", sans-serif;
    font-weight: 400;
    font-size: 36px;
    line-height: 1;
    color: var(--ink);
  }

  .contact {
    position: absolute;
    left: 29px;
    bottom: 14px;
    margin: 0;
    font-family: "Poppins", sans-serif;
    font-size: 7.5px;
    line-height: 11.5px;
    color: var(--muted);
    font-style: normal;
  }
  .contact-url {
    color: #444;
    font-weight: 600;
  }

  .corner-panel {
    position: absolute;
    right: 0;
    bottom: 0;
    width: 290px;
    height: 100px;
    background: linear-gradient(135deg, var(--magenta) 0%, var(--navy) 50%, var(--sky) 100%);
  }
</style>
</head>
<body>
<main class="canvas">
  <section class="sheet sheet--cover">
    <div class="cover-panel" role="img" aria-label="Large brand graphic in magenta, navy and sky blue"></div>
    <p class="cover-url">www.clarevo.co</p>
  </section>

  <section class="sheet sheet--letterhead">
    <div class="brand">
      <span class="brand-dot"></span>
      <h1 class="brand-name">Clarevo</h1>
    </div>

    <address class="contact">
      12000 Rabat, Morocco<br>
      +212 611-482093<br>
      info@clarevo.co<br>
      <span class="contact-url">www.clarevo.co</span>
    </address>

    <div class="corner-panel" role="img" aria-label="Corner brand graphic in magenta, navy and sky blue"></div>
  </section>
</main>
</body>
</html>
```